Window cleaning company in need of leaflet design

Family run business requires leaflet design.
Our company uses water fed pole with pure water which is what the leaflet needs to emphasise on (include a background picture of a water fed pole cleaning a window.)

other services we offer which i would like to include are:
• facia/soffit cleaning.
• Conservatory cleans.
• Gutter clearing which is performed by a gutter vacuum pictures of gutters before and after clean are provided to every customer if they require.
• pressure washing

uploaded company logo to be included on leaflet.
number to include is 07715264389
email address is Rtglasscare@mailbay.test
would also like a facebook symbol included to show we are on social media.
Thank you

Font styles to use
Serif
Sans Serif

Colors
00a990
33a6d7
3276b5
3277b5
34a7d8
87cfc6
33b8a4
cfdfed
85acd3

Requirements
Must have
• We use traditional and water fed pole methods of cleaning. So those hard to reach or awkward to clean windows are not a problem. No need for ladders.

Our water fed pole system uses 100% pure water. This is water that has been de-ironised and de-mineralised to ensue it’s perfectly pure for a spot free finish.

• fully insured

• regular and reliable service
• one off cleans available

Call dean on 07715264389 for a free quote

```html
<!DOCTYPE html>
<html lang="en">
<head>
<meta charset="utf-8">
<title>R.T Glass Care – Window Cleaning Leaflet</title>
<link rel="stylesheet" href="https://fonts.googleapis.com/css2?family=Montserrat:wght@300;400;500;600;700;800;900&display=swap">
<style>
  :root{
    --navy:#24406e;
    --brand-blue:#2f7ac0;
    --mid-blue:#3277b5;
    --sky:#34a7d8;
    --pale:#cfdfed;
    --text-blue:#2c6cb0;
    --para-blue:#4aa3d8;
    --white:#ffffff;
    --photo-stone:#b9a88a;
    --photo-dark:#6f6a5e;
  }
  *{margin:0;padding:0;box-sizing:border-box}
  html,body{width:857px;height:1200px;overflow:hidden;background:#fff}
  body{font-family:'Montserrat',sans-serif}
  .leaflet{position:relative;width:857px;height:1200px;overflow:hidden;background:var(--white)}
  .hero-photo{position:absolute;left:0;top:0;width:857px;height:800px;
    background:linear-gradient(160deg,#8a8170 0%,var(--photo-stone) 35%,#a89779 60%,var(--photo-dark) 100%)}
  .waves{position:absolute;left:0;top:0}
  .brand{position:absolute;left:606px;top:88px;width:218px;text-align:center;
    font-weight:600;font-size:24px;color:var(--navy);letter-spacing:.2px}
  .headline{position:absolute;left:300px;top:280px;width:520px;text-align:center;
    color:var(--white);font-weight:800;font-size:34px;line-height:39px;text-transform:uppercase;
    text-shadow:0 2px 4px rgba(0,0,0,.45)}
  .no-ladders{position:absolute;left:315px;top:437px;width:182px;height:182px;border-radius:50%;
    background:var(--white);padding:8px}
  .no-ladders-inner{width:100%;height:100%;border-radius:50%;background:var(--brand-blue);
    display:flex;flex-direction:column;align-items:center;justify-content:center;color:var(--white)}
  .no-ladders .big{font-weight:800;font-size:72px;line-height:64px;letter-spacing:-2px}
  .no-ladders .small{font-weight:500;font-size:22px;letter-spacing:1px;margin-top:4px}
  .services{position:absolute;left:0;top:785px;width:857px}
  .service{position:absolute;width:170px;text-align:center}
  .service-icon{display:block;margin:0 auto}
  .service-label{margin-top:8px;font-weight:800;font-size:15.5px;line-height:17px;color:var(--text-blue);text-transform:uppercase}
  .purity{position:absolute;left:40px;top:983px;width:777px;text-align:center;
    font-weight:300;font-size:16.5px;line-height:25px;color:var(--para-blue)}
  .assurances{position:absolute;left:0;top:1063px;width:857px;display:flex;justify-content:center;
    font-weight:700;font-size:15.5px;color:var(--text-blue);text-transform:uppercase;letter-spacing:.3px}
  .assurances span{padding:0 12px;border-left:2px solid var(--text-blue);line-height:24px}
  .assurances span:first-child{border-left:none}
  .footer{position:absolute;left:0;top:1108px;width:857px;height:92px;background:var(--brand-blue);color:var(--white)}
  .social-dot{position:absolute;left:54px;top:37px;width:36px;height:36px;border:2px solid var(--white);border-radius:50%}
  .email{position:absolute;left:171px;top:44px;font-size:16px;font-weight:400;letter-spacing:.3px}
  .call{position:absolute;left:531px;top:16px;width:254px;text-align:center}
  .call-label{font-weight:600;font-size:18px;letter-spacing:1px;text-transform:uppercase;position:relative;display:inline-block;padding:0 8px}
  .call-frame{position:absolute;left:0;top:24px;width:254px;height:44px;border:2px solid var(--white);border-top:none;border-radius:0 0 14px 14px}
  .call-frame::before,.call-frame::after{content:"";position:absolute;top:-12px;width:40px;height:12px;border-top:2px solid var(--white)}
  .call-frame::before{left:-2px;border-left:2px solid var(--white);border-radius:14px 0 0 0}
  .call-frame::after{right:-2px;border-right:2px solid var(--white);border-radius:0 14px 0 0}
  .phone{font-weight:800;font-size:31px;line-height:38px;letter-spacing:.5px;margin-top:-2px}
</style>
</head>
<body>
<main class="leaflet">
  <div class="hero-photo" role="img" aria-label="Photo of a window cleaner in a branded hoodie using a red water fed pole to clean an upstairs window of a stone house with a lantern above an arched porch"></div>

  <svg class="waves" width="857" height="1200" viewBox="0 0 857 1200" aria-hidden="true">
    <defs>
      <linearGradient id="swoosh" x1="0" y1="0" x2="1" y2="1">
        <stop offset="0" stop-color="#34a7d8"/>
        <stop offset="1" stop-color="#3277b5"/>
      </linearGradient>
    </defs>
    <path d="M420,0 C500,50 530,150 680,185 C760,205 820,215 857,230 L857,0 Z" fill="#34a7d8"/>
    <path d="M440,0 C520,40 550,130 690,162 C770,180 830,190 857,198 L857,0 Z" fill="#fff"/>
    <path d="M857,405 C760,420 650,480 570,560 C480,650 380,705 240,745 L857,760 Z" fill="url(#swoosh)"/>
    <path d="M0,600 C90,680 200,755 340,770 C450,780 540,755 620,735 L620,820 L0,820 Z" fill="#1e3f73"/>
    <path d="M0,640 C80,700 190,770 330,782 C430,790 520,770 600,752 L600,820 L0,820 Z" fill="#3277b5"/>
    <path d="M0,690 C140,790 380,800 560,752 C680,718 770,700 857,705 L857,1200 L0,1200 Z" fill="#fff"/>
  </svg>

  <div class="brand">R.T Glass Care</div>

  <h1 class="headline">Professional waterfed<br>pole &amp; traditional<br>window cleaning</h1>

  <div class="no-ladders">
    <div class="no-ladders-inner">
      <span class="big">NO</span>
      <span class="small">LADDERS</span>
    </div>
  </div>

  <section class="services">
    <div class="service" style="left:35px">
      <svg class="service-icon" width="136" height="136" viewBox="0 0 136 136" aria-hidden="true">
        <circle cx="68" cy="68" r="66" fill="#fff" stroke="#2f7ac0" stroke-width="2"/>
        <circle cx="68" cy="68" r="60" fill="#2f7ac0"/>
        <g stroke="#fff" stroke-width="4" stroke-linecap="round" fill="none">
          <line x1="42" y1="50" x2="92" y2="34"/><line x1="48" y1="60" x2="88" y2="48"/>
          <path d="M46,104 L78,68 L96,86 Z" fill="#fff"/>
          <line x1="46" y1="104" x2="34" y2="116"/>
        </g>
      </svg>
      <div class="service-label">Facia/Soffit<br>Cleaning</div>
    </div>
    <div class="service" style="left:226px">
      <svg class="service-icon" width="136" height="136" viewBox="0 0 136 136" aria-hidden="true">
        <circle cx="68" cy="68" r="66" fill="#fff" stroke="#2f7ac0" stroke-width="2"/>
        <circle cx="68" cy="68" r="60" fill="#2f7ac0"/>
        <g stroke="#fff" stroke-width="3.5" fill="none" stroke-linejoin="round">
          <path d="M36,60 L56,34 L104,34 L100,60 Z"/>
          <path d="M64,40 L92,40 L90,54 L62,54 Z"/>
          <rect x="36" y="62" width="64" height="30"/>
          <line x1="52" y1="62" x2="52" y2="92"/><line x1="68" y1="62" x2="68" y2="92"/><line x1="84" y1="62" x2="84" y2="92"/>
          <line x1="30" y1="98" x2="106" y2="98"/>
        </g>
      </svg>
      <div class="service-label">Conservatory<br>Cleans</div>
    </div>
    <div class="service" style="left:412px">
      <svg class="service-icon" width="136" height="136" viewBox="0 0 136 136" aria-hidden="true">
        <circle cx="68" cy="68" r="66" fill="#fff" stroke="#2f7ac0" stroke-width="2"/>
        <circle cx="68" cy="68" r="60" fill="#2f7ac0"/>
        <g stroke="#fff" stroke-width="4" fill="none" stroke-linecap="round" stroke-linejoin="round">
          <path d="M34,46 L102,46"/>
          <path d="M34,56 L102,56 L98,70 L38,70 Z"/>
          <path d="M90,70 L90,104"/>
          <path d="M60,70 L60,92"/>
        </g>
      </svg>
      <div class="service-label">Gutter<br>Clearing</div>
    </div>
    <div class="service" style="left:598px">
      <svg class="service-icon" width="136" height="136" viewBox="0 0 136 136" aria-hidden="true">
        <circle cx="68" cy="68" r="66" fill="#fff" stroke="#2f7ac0" stroke-width="2"/>
        <circle cx="68" cy="68" r="60" fill="#2f7ac0"/>
        <g stroke="#fff" stroke-width="4" fill="none" stroke-linecap="round">
          <rect x="34" y="66" width="14" height="30" rx="3" fill="#fff"/>
          <path d="M48,80 C60,80 60,60 72,60 L96,84"/>
          <line x1="102" y1="86" x2="108" y2="84"/><line x1="102" y1="92" x2="110" y2="94"/><line x1="98" y1="96" x2="102" y2="102"/>
          <line x1="30" y1="102" x2="112" y2="102"/>
        </g>
      </svg>
      <div class="service-label">Pressure<br>Washing</div>
    </div>
  </section>

  <p class="purity">Our water fed pole system uses 100% pure water. This is water that has been de-ironised and de-mineralised to ensue it’s perfectly pure for a spot free finish.</p>

  <div class="assurances">
    <span>Fully insured</span>
    <span>Regular and reliable service</span>
    <span>One off cleans available</span>
  </div>

  <footer class="footer">
    <div class="social-dot" aria-label="Find us on social media"></div>
    <div class="email">rtglasscare@mailbay.test</div>
    <div class="call">
      <div class="call-frame"></div>
      <div class="call-label">Call Dean</div>
      <div class="phone">077 1526 4389</div>
    </div>
  </footer>
</main>
</body>
</html>
```